Webdesign für Projektmanagement
Zielgruppe
Projektmanagement und Projektsteuerung von Bauvorhaben für Projektentwickler und Bauträger.
Wesentliche Bereiche sind Wirtschaftliche Steuerung, Steuerung der Baustelle und Bauabläufe sowie Steuerung der Marketing und Vertriebsaktivitäten.
Aufgabenstellung
Orientierung am Logo. Logo und Visitenkarte liegen bei. Schriftart Prelo und Prelo Slab.

```html
<!DOCTYPE html>
<html lang="de">
<head>
<meta charset="utf-8">
<title>Velhorst Real Estate – Projektmanagement</title>
<link href="https://fonts.googleapis.com/css2?family=Raleway:ital,wght@0,300;0,400;0,600;0,700;0,800;1,400&display=swap" rel="stylesheet">
<style>
  :root {
    --stage: #0a2441;
    --navy: #0c2746;
    --navy-deep: #081b30;
    --gold: #a8904a;
    --white: #ffffff;
    --card: #f1f1f1;
    --text: #3a3a3a;
    --rule: #ececec;
  }
  * { box-sizing: border-box; margin: 0; padding: 0; }
  html, body {
    width: 1036px; height: 1200px; overflow: hidden;
    background: var(--stage);
    font-family: "Raleway", Arial, sans-serif;
  }
  .site {
    position: absolute; left: 18px; top: 312px;
    width: 1000px; height: 576px;
    overflow: hidden;
  }
  .hero-photo {
    position: absolute; left: 138px; top: 0; right: 0; bottom: 0;
    background:
      linear-gradient(180deg, rgba(14,38,66,0.92) 0%, rgba(22,48,78,0.75) 40%, rgba(30,40,52,0.85) 75%, rgba(14,22,32,0.95) 100%),
      linear-gradient(90deg, #1a3552 0%, #2a4660 60%, #3a5268 100%);
  }
  .sidebar {
    position: absolute; left: 0; top: 0; width: 138px; height: 576px;
    background: var(--white);
  }
  .brand {
    position: absolute; left: 23px; top: 62px;
    display: flex; align-items: center; gap: 6px;
  }
  .brand-mark { width: 8px; height: 8px; background: var(--navy); }
  .brand-name {
    font-weight: 700; font-size: 17px; color: var(--navy);
    line-height: 1; letter-spacing: 0.5px;
  }
  .nav { position: absolute; left: 0; top: 141px; width: 138px; list-style: none; border-top: 1px solid var(--rule); }
  .nav li {
    height: 30.6px; border-bottom: 1px solid var(--rule);
    display: flex; align-items: center; justify-content: space-between;
    padding: 0 20px 0 23px;
    font-size: 9px; color: #222; letter-spacing: 0.3px;
  }
  .nav li.active { color: var(--gold); font-weight: 700; }
  .nav .chev { color: var(--gold); font-size: 9px; }
  .nav .search { justify-content: flex-start; gap: 8px; color: #888; font-style: italic; }
  .social { position: absolute; left: 0; width: 138px; top: 547px; display: flex; justify-content: center; gap: 11px; }
  .social span { width: 8px; height: 8px; border-radius: 50%; background: var(--navy); }
  .topbar {
    position: absolute; left: 138px; right: 0; top: 0; height: 30px;
    background: rgba(10,34,60,0.55);
    display: flex; justify-content: flex-end; align-items: center; gap: 16px;
    padding-right: 18px;
    font-size: 8.5px; color: var(--white);
  }
  .topbar .item { display: flex; align-items: center; gap: 5px; }
  .topbar svg { width: 9px; height: 9px; fill: none; stroke: var(--gold); stroke-width: 1.4; }
  .overline { position: absolute; left: 204px; top: 132px; font-weight: 700; font-size: 15.5px; color: var(--gold); letter-spacing: 0.2px; }
  .headline { position: absolute; left: 202px; top: 170px; font-weight: 300; font-size: 49px; line-height: 56px; color: var(--white); letter-spacing: 0.5px; }
  .cards { position: absolute; left: 206px; top: 376px; display: flex; gap: 9px; }
  .card { position: relative; width: 235px; height: 141px; background: var(--card); padding: 10px 12px 0 12px; }
  .card-kicker { font-style: italic; font-size: 8.5px; color: #666; }
  .card-title { margin-top: 8px; font-size: 9.6px; line-height: 13px; color: var(--gold); font-weight: 400; }
  .card-body { margin-top: 7px; font-size: 8.2px; line-height: 13px; color: var(--text); }
  .card-more {
    position: absolute; right: 0; bottom: 0; width: 76px; height: 20px;
    background: var(--navy); color: var(--white);
    font-size: 7.5px; font-weight: 700; letter-spacing: 0.4px;
    display: flex; align-items: center; justify-content: center;
  }
  .footer {
    position: absolute; left: 138px; right: 0; bottom: 0; height: 35px;
    background: rgba(8,20,34,0.6);
    display: flex; align-items: center; justify-content: center;
    font-size: 9px; color: #d9d9d9;
  }
</style>
</head>
<body>
<div class="site">
  <div class="hero-photo" role="img" aria-label="Abendliche Stadtansicht von Düsseldorf mit Fernsehturm und Skyline"></div>

  <header class="topbar">
    <span class="item"><svg viewBox="0 0 10 10"><path d="M2 1 L4 1 L4.6 3 L3.4 4 Q4.6 6 6 6.6 L7 5.4 L9 6 L9 8 Q5 9 1 3 Z"/></svg>+49 (0)211 - 390 215 48</span>
    <span class="item"><svg viewBox="0 0 10 10"><circle cx="5" cy="5" r="4"/><path d="M5 2.6 V5 L6.6 6"/></svg>Mo - Fr 9:00 - 18:00</span>
    <span class="item"><svg viewBox="0 0 10 10"><rect x="1" y="2.5" width="8" height="5.5"/><path d="M1 2.5 L5 5.8 L9 2.5"/></svg>info@velhorst-re.de</span>
    <span class="item"><svg viewBox="0 0 10 10"><path d="M5 9.2 Q1.8 5.6 1.8 3.8 A3.2 3.2 0 0 1 8.2 3.8 Q8.2 5.6 5 9.2 Z"/><circle cx="5" cy="3.8" r="1"/></svg>Lindenhofstr. 21, 40211 Düsseldorf</span>
  </header>

  <aside class="sidebar">
    <div class="brand">
      <span class="brand-mark"></span>
      <span class="brand-name">Velhorst</span>
    </div>
    <ul class="nav">
      <li class="active">HOME</li>
      <li>LEISTUNGEN</li>
      <li>ÜBER UNS <span class="chev">›</span></li>
      <li>PROJEKTE <span class="chev">›</span></li>
      <li>PARTNER</li>
      <li>KONTAKT</li>
      <li class="search"><svg width="8" height="8" viewBox="0 0 10 10" fill="none" stroke="#a8904a" stroke-width="1.6"><circle cx="4" cy="4" r="3"/><path d="M6.3 6.3 L9 9"/></svg>Suchen</li>
    </ul>
    <div class="social" aria-label="Soziale Netzwerke"><span></span><span></span><span></span><span></span></div>
  </aside>

  <p class="overline">PROJEKTMANAGEMENT &amp; PROJEKTSTEUERUNG</p>
  <h1 class="headline">WIR REALISIEREN<br>BAUVORHABEN</h1>

  <section class="cards">
    <article class="card">
      <p class="card-kicker">Betriebswirtschaftliche Planung</p>
      <h2 class="card-title">STET CLITA KASD GUBERGREN NO SEA TAKIMATA SANCTUS EST LOREM IPSUM</h2>
      <p class="card-body">Lorem ipsum dolor sit amet, consetetur sadipscing elitr, sed diam nonumy eirmod tempor invidunt ut labore et dolore magna aliquyam erat, sed diam voluptua.</p>
      <span class="card-more">WEITERLESEN</span>
    </article>
    <article class="card">
      <p class="card-kicker">Steuerung der baulichen Umsetzung</p>
      <h2 class="card-title">STET CLITA KASD GUBERGREN NO SEA TAKIMATA SANCTUS EST LOREM IPSUM</h2>
      <p class="card-body">Lorem ipsum dolor sit amet, consetetur sadipscing elitr, sed diam nonumy eirmod tempor invidunt ut labore et dolore magna aliquyam erat, sed diam voluptua.</p>
      <span class="card-more">WEITERLESEN</span>
    </article>
    <article class="card">
      <p class="card-kicker">Marketing und Vertrieb</p>
      <h2 class="card-title">STET CLITA KASD GUBERGREN NO SEA TAKIMATA SANCTUS EST LOREM IPSUM</h2>
      <p class="card-body">Lorem ipsum dolor sit amet, consetetur sadipscing elitr, sed diam nonumy eirmod tempor invidunt ut labore et dolore magna aliquyam erat, sed diam voluptua.</p>
      <span class="card-more">WEITERLESEN</span>
    </article>
  </section>

  <footer class="footer">© 2017 Velhorst Real Estate GmbH - Impressum</footer>
</div>
</body>
</html>
```